Flyer for longday centre (Childcare Centre)

We need a marketing flyer for our long day (Childcare) centre targeting childcare enrolments for 2016.

The name of the childcare is: Wexbury Vale Early Childhood Learning Centre
Location: will be provided later
Telephone: will be provided later
Email: will be provided later

The message of the flyer should have limited places now available for 2016. Enrol now.

Target Market(s)

Parents and Families

Industry/Entity Type

Childcare

Font styles to use
Sans Serif

Requirements
Must have
• Come and see why more and more families are switching to Wexbury Vale.
• We invite parents to come along to explore our facilities and our children's programs.
• We also run a government approved and funded Kindergarten program.
Nice to have
• Opening hours: 6am to 6:30pm Monday to Friday

```html
<!DOCTYPE html>
<html lang="en">
<head>
<meta charset="utf-8">
<title>Wexbury Vale Early Childhood Learning Centre – Enrol Now</title>
<link rel="stylesheet" href="https://fonts.googleapis.com/css2?family=PT+Sans:wght@400;700&display=swap">
<style>
  :root {
    --paper: #ffffff;
    --ink: #1a1a1a;
    --brand-green: #1f9a3c;
    --accent-red: #e0262b;
    --photo-warm: #d9b79a;
    --photo-cool: #a9c4d8;
    --photo-bright: #d65a4a;
    --confetti-lilac: #ece4f4;
    --confetti-sky: #e3f0f8;
    --confetti-peach: #fbeee4;
    --confetti-mint: #e8f5ea;
    --stage: #f2f2f2;
  }
  html, body {
    margin: 0;
    padding: 0;
    width: 900px;
    height: 1200px;
    overflow: hidden;
    background: var(--stage);
  }
  .flyer {
    position: relative;
    width: 900px;
    height: 1200px;
    background: var(--paper);
    font-family: "PT Sans", Arial, sans-serif;
    color: var(--ink);
    overflow: hidden;
  }
  .confetti-field {
    position: absolute;
    inset: 0;
    background:
      radial-gradient(circle at 12% 20%, var(--confetti-lilac) 0, transparent 32%),
      radial-gradient(circle at 85% 12%, var(--confetti-sky) 0, transparent 34%),
      radial-gradient(circle at 20% 88%, var(--confetti-peach) 0, transparent 36%),
      radial-gradient(circle at 88% 80%, var(--confetti-mint) 0, transparent 36%),
      radial-gradient(circle at 50% 55%, var(--confetti-sky) 0, transparent 45%),
      var(--paper);
  }
  .brand {
    position: absolute;
    top: 60px;
    left: 80px;
    display: flex;
    align-items: center;
    gap: 16px;
  }
  .brand-dot {
    width: 58px;
    height: 58px;
    border-radius: 50%;
    background: var(--brand-green);
    flex: none;
  }
  .brand-name {
    font-weight: 700;
    color: var(--brand-green);
    font-size: 25px;
    line-height: 1.2;
    margin: 0;
    max-width: 320px;
  }
  .gallery {
    position: absolute;
    top: 240px;
    left: 0;
    width: 900px;
    height: 520px;
  }
  .message {
    position: absolute;
    top: 740px;
    left: 70px;
    width: 760px;
    text-align: center;
  }
  .headline {
    margin: 0;
    font-size: 54px;
    font-weight: 400;
    line-height: 1.1;
  }
  .availability {
    margin: 4px 0 0;
    font-size: 36px;
    font-weight: 700;
    color: var(--brand-green);
    line-height: 1.2;
  }
  .hours-label {
    margin: 2px 0 0;
    font-size: 40px;
    font-weight: 400;
    line-height: 1.2;
  }
  .hours {
    margin: 8px 0 0;
    font-size: 50px;
    font-weight: 400;
    color: var(--brand-green);
    line-height: 1.15;
    white-space: nowrap;
  }
  .invitation {
    margin: 14px 0 0;
    font-size: 28px;
    line-height: 1.32;
    text-align: justify;
    text-align-last: center;
  }
</style>
</head>
<body>
<main class="flyer">
  <div class="confetti-field" role="img" aria-label="Soft pastel confetti and streamer pattern"></div>

  <header class="brand">
    <span class="brand-dot"></span>
    <p class="brand-name">Wexbury Vale Early Childhood Learning Centre</p>
  </header>

  <svg class="gallery" viewBox="0 0 900 520" xmlns="http://www.w3.org/2000/svg">
    <defs>
      <linearGradient id="photo-left" x1="0" y1="0" x2="1" y2="1">
        <stop offset="0" stop-color="var(--photo-cool)"/>
        <stop offset="1" stop-color="var(--photo-warm)"/>
      </linearGradient>
      <linearGradient id="photo-centre" x1="0" y1="0" x2="1" y2="1">
        <stop offset="0" stop-color="#e8d6c4"/>
        <stop offset="1" stop-color="var(--photo-warm)"/>
      </linearGradient>
      <linearGradient id="photo-right" x1="0" y1="0" x2="1" y2="1">
        <stop offset="0" stop-color="#c9d8c6"/>
        <stop offset="1" stop-color="var(--photo-bright)"/>
      </linearGradient>
    </defs>

    <path class="cloud-outline" d="M-10,330 C30,250 110,230 170,250 C190,150 300,110 370,150 C420,40 560,40 610,130 C680,90 770,130 780,210 C850,200 910,250 910,300"
          fill="none" stroke="var(--brand-green)" stroke-width="9" stroke-linecap="round"/>

    <path class="support-band" d="M40,330 Q450,470 860,330" fill="none" stroke="var(--brand-green)" stroke-width="22"/>

    <g role="img" aria-label="Photo of a child playing with educator at a table">
      <circle cx="160" cy="300" r="100" fill="var(--brand-green)"/>
      <circle cx="160" cy="300" r="88" fill="url(#photo-left)"/>
      <circle cx="160" cy="300" r="82" fill="none" stroke="var(--accent-red)" stroke-width="3" stroke-dasharray="6 5"/>
    </g>
    <g role="img" aria-label="Photo of a toddler playing with building blocks">
      <circle cx="730" cy="300" r="108" fill="var(--brand-green)"/>
      <circle cx="730" cy="300" r="96" fill="url(#photo-right)"/>
      <circle cx="730" cy="300" r="90" fill="none" stroke="var(--accent-red)" stroke-width="3" stroke-dasharray="6 5"/>
    </g>
    <g role="img" aria-label="Photo of a young child reaching for toys">
      <circle cx="450" cy="270" r="180" fill="var(--brand-green)"/>
      <circle cx="450" cy="270" r="166" fill="url(#photo-centre)"/>
      <circle cx="450" cy="270" r="158" fill="none" stroke="var(--accent-red)" stroke-width="3" stroke-dasharray="7 6"/>
    </g>
  </svg>

  <section class="message">
    <h1 class="headline">Enrol now</h1>
    <p class="availability">Limited places now available for 2016</p>
    <p class="hours-label">Opening hours</p>
    <p class="hours">6am to 6:30pm Monday to Friday</p>
    <p class="invitation">Come and see why more and more families are switching to Wexbury Vale. We invite parents to come along to explore our facilities and our children's programs. We also run a government approved and funded Kindergarten program.</p>
  </section>
</main>
</body>
</html>
```